Nimbo58.com.au Website and company image design

We are looking for an exceptional website designer / company to work with our new Australian Hosting Company

Nimbo58 is a new Cloud Hosting company launching in Australia that provides Scalable, On Demand computing resources to the Australian Market Place. Scalable, On Demand ocmputing is a nice way of saying fully scalable / redundant Virtual Private Server.

We require a full company image to be developed along with a Logo and Website. There is scope for ongoing development (preferred) for the successful candidate.

Website developement will require extensive jQuery ability (sliders for ordering etc (see: http://www.hostrix-example.com.au/virtual-dedicated-servers/253/zar_vps.html).

Please communicate directly with me to establish full website scope and request further documentation / content.

Target Market(s)

Website Designers, programmers, technicians and large companies

Industry/Entity Type

It Company

Requirements
Must have
• Slider ordering system such as http://www.hostrix-example.com.au/virtual-dedicated-servers/253/zar_vps.html

Nice to have
• CMS backend system
Should not have
• Should NOT be a monster template copy!!!

```html
<!DOCTYPE html>
<html lang="en">
<head>
<meta charset="utf-8">
<title>Nimbo58 – Australian Web Hosting, VPS &amp; Dedicated Servers</title>
<link rel="stylesheet" href="https://fonts.googleapis.com/css2?family=Arimo:wght@400;700&family=Montserrat:ital,wght@0,400;0,500;0,600;0,700;1,400&display=swap">
<style>
:root{
  --brand-blue:#1a7fc1;
  --hero-blue:#5d9bc9;
  --green:#6cab2c;
  --green-dark:#4f8d17;
  --red:#d0131a;
  --ink:#222;
  --text:#555;
  --muted:#888;
  --line:#d6d6d6;
  --panel:#fff;
  --stage:#ebebeb;
  --nav-top:#444;
  --nav-bottom:#1c1c1c;
  --tick:#4a9a1e;
}
*{box-sizing:border-box;margin:0;padding:0}
html,body{width:696px;height:1200px;overflow:hidden}
body{position:relative;background:#fff;font-family:"Arimo",Arial,sans-serif;color:var(--text);font-size:8px}
.abs{position:absolute}
ul{list-style:none}

/* header */
.brand{left:82px;top:6px;width:52px;height:52px;background:var(--brand-blue);border-radius:3px;color:#fff;font:700 10px "Montserrat",sans-serif;display:flex;align-items:flex-end;justify-content:center;padding-bottom:8px}
.top-links{right:84px;top:10px;display:flex;align-items:center;gap:6px;font-size:8px;color:#444}
.top-links .sep{color:#aaa}
.top-links .phone{font:600 9.5px "Montserrat",sans-serif;color:#222;margin:0 4px}
.btn-signup{background:var(--green);color:#fff;padding:2px 5px;border-radius:2px;font-size:7.5px}
.btn-login{background:#e2e2e2;color:#555;padding:2px 5px;border-radius:2px;font-size:7.5px;border:1px solid #ccc}
.main-nav{left:138px;top:36px;width:475px;height:20px;background:linear-gradient(var(--nav-top),var(--nav-bottom));border-radius:2px;display:flex;justify-content:space-between;align-items:center;padding:0 8px 0 10px}
.main-nav a{color:#fff;font:500 7.5px "Montserrat",sans-serif;text-decoration:none}

/* hero */
.hero{left:82px;top:62px;width:531px;height:188px;background:linear-gradient(#f7f7f7,#dcdcdc);border:1px solid #d2d2d2;border-radius:3px}
.hero-kicker{left:25px;top:20px;font:italic 400 18px "Montserrat",sans-serif;color:#666}
.hero-title{left:23px;top:37px;font:700 25px "Montserrat",sans-serif;color:var(--hero-blue);letter-spacing:-.3px}
.hero-copy{left:24px;top:75px;width:280px;font-size:8.5px;line-height:12.3px;color:#666}
.btn-quote{left:103px;top:141px;width:139px;height:24px;border-radius:12px;background:linear-gradient(#fafafa,#d8d8d8);border:1px solid #bbb;display:flex;align-items:center;justify-content:space-between;padding:0 6px 0 11px;font:400 9.5px "Montserrat",sans-serif;color:#444}
.hero-art{left:312px;top:12px;width:148px;height:174px;border-radius:40px 40px 50px 50px;background:radial-gradient(ellipse at 50% 35%,#5a5a5a,#b9b9b9 55%,#d6d6d6 80%)}

/* stage */
.stage{left:82px;top:258px;width:531px;height:712px;background:var(--stage)}
.box{background:var(--panel);border:1px solid #dcdcdc;border-radius:3px;box-shadow:0 1px 2px rgba(0,0,0,.08)}

/* sidebar */
.domain-search{left:88px;top:264px;width:95px;height:92px}
.side-title{font:700 9.5px "Arimo",sans-serif;color:var(--ink);line-height:11px}
.domain-search .side-title{position:absolute;left:8px;top:10px}
.tld-select{left:7px;top:37px;width:82px;height:17px;border:1px solid #c9c9c9;border-radius:2px;font-size:7.5px;color:#555;display:flex;align-items:center;justify-content:flex-end;padding-right:4px;gap:3px}
.btn-check{left:10px;top:65px;width:75px;height:18px;background:linear-gradient(#3d9be0,var(--brand-blue));border-radius:3px;color:#fff;font-size:7.5px;font-weight:700;display:flex;align-items:center;justify-content:center}
.aussie{left:88px;top:364px;width:95px;height:218px}
.aussie .side-title{position:absolute;left:0;top:9px;width:100%;text-align:center}
.aussie-map{left:12px;top:27px;width:70px;height:58px;border-radius:8px;background:linear-gradient(135deg,#2e5fae,#1e3f80)}
.promise{left:6px;width:83px;height:25px;background:linear-gradient(#f4f4f4,#dedede);border:1px solid #c2c2c2;border-radius:2px;font-size:6.5px;line-height:7.5px;color:#444;text-align:center;display:flex;align-items:center;justify-content:center}
.spam{left:88px;top:592px;width:95px;height:134px}
.spam .side-title{position:absolute;left:0;top:8px;width:100%;text-align:center;color:var(--brand-blue)}
.spam-chart{left:17px;top:23px}
.spam-caption{left:0;top:88px;width:100%;text-align:center;font-size:6.5px;color:var(--brand-blue)}
.spam-count{left:6px;top:100px;width:83px;height:29px;background:linear-gradient(#f4f4f4,#dedede);border:1px solid #c2c2c2;border-radius:2px;text-align:center;font-size:6.5px;color:#444;padding-top:3px}
.spam-count strong{display:block;color:var(--red);font-size:9px}

/* plan cards */
.plan{top:265px;width:96px;height:128px;text-align:center}
.plan-head{height:22px;background:linear-gradient(#8cc63f,var(--green-dark));color:#fff;font:600 8.5px "Montserrat",sans-serif;display:flex;align-items:center;justify-content:center;border-radius:2px 2px 0 0}
.plan-price{height:27px;border-bottom:1px solid #e3e3e3;display:flex;align-items:center;justify-content:center;gap:2px;font-size:6.5px;color:#555}
.plan-price b{font:700 13px "Montserrat",sans-serif;color:var(--red)}
.plan-list{padding-top:7px;font-size:6.5px;line-height:8.5px;color:#555;height:50px}
.btn-more{margin:6px auto 0;width:58px;height:14px;border-radius:7px;background:linear-gradient(#f6f6f6,#d6d6d6);border:1px solid #bbb;font-size:6.5px;color:#444;display:flex;align-items:center;justify-content:center}

/* content */
.intro-title{left:195px;top:407px;font:500 13.5px "Montserrat",sans-serif;color:var(--ink)}
.intro-copy{left:195px;top:430px;width:405px;font-size:7.5px;line-height:10px;color:#666}
.build-title{left:195px;top:478px;font:700 9.5px "Arimo",sans-serif;color:var(--red)}
.builder{left:198px;top:497px;width:300px;height:258px}
.builder h3{position:absolute;left:11px;top:12px;font:600 9.5px "Montserrat",sans-serif;color:var(--ink)}
.os-select{left:10px;top:30px;width:223px;height:17px;border:1px solid #c8c8c8;border-radius:2px;background:linear-gradient(#fff,#eee);font-size:7.5px;color:#444;display:flex;align-items:center;justify-content:space-between;padding:0 5px}
.customise{left:11px;top:58px;font-size:7px;color:var(--red)}
.slider{left:10px;width:277px;height:30px}
.slider-label{position:absolute;left:6px;top:0;font-size:7.5px;color:#333}
.slider-label b{font-weight:700}
.slider-label span{color:#666}
.slider-value{position:absolute;right:0;top:0;font-size:7.5px;color:#555}
.slider-track{position:absolute;left:4px;right:0;top:16px;height:4px;border-radius:2px;background:#e4e4e4;border:1px solid #cfcfcf}
.slider-knob{position:absolute;left:0;top:11px;width:12px;height:13px;border-radius:2px;background:linear-gradient(#e02a2a,#a70c0c)}
.testimonial{left:507px;top:497px;width:95px;height:193px;padding:7px 9px}
.testimonial h4{font:700 9.5px "Arimo",sans-serif;color:var(--ink);line-height:11px}
.testimonial blockquote{margin-top:17px;font-style:italic;font-size:6.7px;line-height:10px;color:#666}
.testimonial cite{display:block;margin-top:16px;font-style:normal;font-size:6.5px;line-height:8px;color:#333;padding-left:2px}
.price-bar{left:222px;top:763px;width:244px;height:26px;display:flex;box-shadow:0 1px 2px rgba(0,0,0,.15)}
.price-total{width:155px;background:#fff;border:1px solid #ccc;display:flex;align-items:center;justify-content:center;font:600 10.5px "Montserrat",sans-serif;color:#333}
.btn-software{flex:1;background:linear-gradient(#e0231d,#b30d0d);color:#fff;font:600 8px "Montserrat",sans-serif;display:flex;align-items:center;justify-content:center;gap:3px}
.why{left:198px;top:800px;width:299px;height:151px;padding:11px 10px}
.why h3{font:600 9.5px "Montserrat",sans-serif;color:var(--ink);margin-bottom:4px}
.why li{display:flex;align-items:center;gap:6px;height:13px;font-size:7.3px;color:#666}
.ribbon{left:357px;top:935px;width:143px;height:17px;background:var(--brand-blue);color:#fff;font-size:7.3px;display:flex;align-items:center;justify-content:center;clip-path:polygon(7px 0,100% 0,100% 100%,7px 100%,0 50%)}

/* partners */
.partners{left:100px;top:986px;width:495px;height:34px;display:flex;justify-content:space-between;align-items:center}
.partner{height:22px;background:#c9c9c9;border-radius:3px}

/* footer */
.site-footer{left:82px;top:1037px;width:531px;height:148px;border:1px solid #ddd;border-radius:3px;background:#fff}
.foot-col{top:11px}
.foot-col h5{font:700 7.5px "Arimo",sans-serif;color:var(--ink);margin-bottom:3px}
.foot-col li{font-size:6.4px;line-height:9.1px;color:#5a7fa6}
.foot-divider{left:393px;top:10px;width:1px;height:128px;background:#e1e1e1}
.social{left:405px;top:11px}
.social h5{font:700 7.5px "Arimo",sans-serif;color:var(--ink);margin-bottom:8px}
.social-row{display:flex;align-items:center;gap:5px;font-size:6.4px;color:#5a7fa6;margin-bottom:7px}
.social-square{width:19px;height:19px;border-radius:2px}
.copyright{left:406px;top:121px;font-size:6.4px;line-height:9px;color:#777}
.copyright a{color:#5a7fa6;text-decoration:none}
</style>
</head>
<body>

<header>
  <div class="abs brand">Nimbo58</div>
  <nav class="abs top-links">
    <span>Home</span><span class="sep">|</span><span>Support</span><span class="sep">|</span><span>Contact us</span>
    <span class="phone">1300 55 0199</span>
    <span class="btn-signup">Sign up</span>
    <span class="btn-login">Log in</span>
  </nav>
  <nav class="abs main-nav">
    <a>Domains</a><a>Web Hosting</a><a>Virtual Servers</a><a>Dedicated Servers</a><a>Resellers</a><a>About Us</a><a>Support</a>
  </nav>
</header>

<section class="abs hero">
  <p class="abs hero-kicker">Lorem ipsum dolor</p>
  <h1 class="abs hero-title">Duis aute irure dolor</h1>
  <p class="abs hero-copy">Lorem ipsum dolor sit amet, consectetur adipisicing elit, sed do eiusmod tempor incididunt ut labore et dolore magna aliqua. Ut enim ad minim veniam, quis nostrud exercitation ullamco laboris nisi ut aliquip ex ea commodo consequat.</p>
  <div class="abs btn-quote"><span>Request a quote now!</span>
    <svg width="9" height="10" viewBox="0 0 9 10"><path d="M2 1l5 4-5 4" fill="none" stroke="#555" stroke-width="1.6"/></svg>
  </div>
  <div class="abs hero-art" role="img" aria-label="Illustration of two server towers standing on a stack of silver cloud-shaped discs"></div>
</section>

<div class="abs stage"></div>

<aside>
  <div class="abs box domain-search">
    <p class="side-title">Domain Name<br>Search</p>
    <div class="abs tld-select">.com.au <svg width="6" height="4" viewBox="0 0 6 4"><path d="M0 0h6L3 4z" fill="var(--brand-blue)"/></svg></div>
    <div class="abs btn-check">Check Domain</div>
  </div>

  <div class="abs box aussie">
    <p class="side-title">100% Australian</p>
    <div class="abs aussie-map" role="img" aria-label="Map of Australia filled with the Australian flag"></div>
    <div class="abs promise" style="top:88px">30 day money-back<br>guarantee</div>
    <div class="abs promise" style="top:121px">24x7 Emergency<br>Phone Support</div>
    <div class="abs promise" style="top:152px">99.9% Service Level<br>Agreement</div>
    <div class="abs promise" style="top:185px">Australia's largest<br>provider of VPS<br>Servers</div>
  </div>

  <div class="abs box spam">
    <p class="side-title">Spam Filtering</p>
    <svg class="abs spam-chart" width="60" height="60" viewBox="0 0 60 60" aria-label="Pie chart of spam versus email">
      <circle cx="30" cy="30" r="29" fill="var(--brand-blue)"/>
      <path d="M30 30L59 32A29 29 0 0 1 46 54Z" fill="var(--red)" stroke="#fff" stroke-width="1.2"/>
    </svg>
    <p class="abs spam-caption">Todays Spam vs Email</p>
    <div class="abs spam-count"><strong>153,074</strong>Spam blocked today</div>
  </div>
</aside>

<main>
  <article class="abs box plan" style="left:193px">
    <div class="plan-head">Domain Names</div>
    <div class="plan-price">from <b>$14.95</b> /year</div>
    <p class="plan-list">Register your domains for<br>.com.au .net.au, .org.au,<br>.co.nz, .net.nz, .com, .net,<br>.org and many more</p>
    <div class="btn-more">MORE INFO</div>
  </article>
  <article class="abs box plan" style="left:297px">
    <div class="plan-head">Web Hosting</div>
    <div class="plan-price">from <b>$6.95</b> /month</div>
    <p class="plan-list">Reseller Web Hosting<br>Fenestra Website Hosting<br>Penguix Website Hosting<br>FREE Application Vault<br>FREE Email/Webmail</p>
    <div class="btn-more">MORE INFO</div>
  </article>
  <article class="abs box plan" style="left:402px">
    <div class="plan-head">VPS Hosting</div>
    <div class="plan-price">from <b>$9.95</b> /month</div>
    <p class="plan-list">Vortexa VPS<br>HyperVista VPS<br>Citra Zar VPS<br>VirtuWare VPS<br>Plexo &amp; CtrlDesk</p>
    <div class="btn-more">MORE INFO</div>
  </article>
  <article class="abs box plan" style="left:507px">
    <div class="plan-head">Dedicated Servers</div>
    <div class="plan-price">from <b>$99.95</b> /month</div>
    <p class="plan-list">Delta &amp; Supernova Servers<br>Value i Series Servers<br>Same Day Servers<br>Hourly Backup<br>SERVER SPECIALS</p>
    <div class="btn-more">MORE INFO</div>
  </article>

  <h2 class="abs intro-title">Australian Web Hosting, VPS &amp; Dedicated Servers</h2>
  <p class="abs intro-copy">Lorem ipsum dolor sit amet, consectetur adipisicing elit, sed do eiusmod tempor incididunt ut labore et dolore magna aliqua. Ut enim ad minim veniam, quis nostrud exercitation ullamco laboris nisi ut aliquip ex ea commodo consequat. Duis aute irure dolor in reprehenderit in voluptate velit esse cillum dolore eu fugiat nulla pariatur. Excepteur sint occaecat cupidatat non proident, sunt in culpa qui officia deserunt mollit anim id est laborum.</p>
  <h3 class="abs build-title">Build Your Server</h3>

  <section class="abs box builder">
    <h3>Select your Operating System</h3>
    <div class="abs os-select"><span>Altos 4</span><svg width="7" height="4" viewBox="0 0 7 4"><path d="M0 0h7L3.5 4z" fill="#555"/></svg></div>
    <p class="abs customise">Customise your System</p>
    <div class="abs slider" style="top:83px"><p class="slider-label"><b>CPU cores</b> <span>($15.00 per Core)</span></p><p class="slider-value">1 Cores</p><div class="slider-track"></div><div class="slider-knob"></div></div>
    <div class="abs slider" style="top:118px"><p class="slider-label"><b>Disk Space</b> <span>($0.60 per GB)</span></p><p class="slider-value">25 GB</p><div class="slider-track"></div><div class="slider-knob"></div></div>
    <div class="abs slider" style="top:152px"><p class="slider-label"><b>Dedicated RAM</b> <span>($15.00 per GB)</span></p><p class="slider-value">.5 GB</p><div class="slider-track"></div><div class="slider-knob"></div></div>
    <div class="abs slider" style="top:187px"><p class="slider-label"><b>Premium Bandwith</b> <span>($0.70 per GB)</span></p><p class="slider-value">50 GB</p><div class="slider-track"></div><div class="slider-knob"></div></div>
    <div class="abs slider" style="top:220px"><p class="slider-label"><b>IP Addresses</b> <span>($3.50 per IP Address)</span></p><p class="slider-value">1 IP</p><div class="slider-track"></div><div class="slider-knob"></div></div>
  </section>

  <aside class="abs box testimonial">
    <h4>What our<br>Customers<br>Say...</h4>
    <blockquote>Lorem ipsum dolor sit amet, consectetur adipisicing elit, sed do eiusmod tempor incididunt ut labore et dolore magna aliqua. Ut enim ad minim veniam, quis nostrud exercitation .</blockquote>
    <cite>Jordan Pell<br>Brightline IT Pty Ltd</cite>
  </aside>

  <div class="abs price-bar">
    <div class="price-total">Monthly Price: $18.50</div>
    <div class="btn-software">Select Software <svg width="8" height="11" viewBox="0 0 8 11"><path d="M1.5 1l5 4.5-5 4.5" fill="none" stroke="#fff" stroke-width="2"/></svg></div>
  </div>

  <section class="abs box why">
    <h3>Why Choose Nimbo58 for your domain names?</h3>
    <ul>
      <li><svg width="8" height="7" viewBox="0 0 8 7"><path d="M1 3.5l2 2L7 1" fill="none" stroke="var(--tick)" stroke-width="1.8"/></svg>Duis placerat eros ut metus suscipit non ultricies blandit.</li>
      <li><svg width="8" height="7" viewBox="0 0 8 7"><path d="M1 3.5l2 2L7 1" fill="none" stroke="var(--tick)" stroke-width="1.8"/></svg>Nunc elementum lacus in turpis accumsan ut feugiat.</li>
      <li><svg width="8" height="7" viewBox="0 0 8 7"><path d="M1 3.5l2 2L7 1" fill="none" stroke="var(--tick)" stroke-width="1.8"/></svg>Ut vitae velit id nisi dictum fermentum et nec arcu.</li>
      <li><svg width="8" height="7" viewBox="0 0 8 7"><path d="M1 3.5l2 2L7 1" fill="none" stroke="var(--tick)" stroke-width="1.8"/></svg>Mauris vitae est at odio sollicitudin ultrices blandit eget.</li>
      <li><svg width="8" height="7" viewBox="0 0 8 7"><path d="M1 3.5l2 2L7 1" fill="none" stroke="var(--tick)" stroke-width="1.8"/></svg>Morbi id risus ac nulla vehicula commodo nec eget lorem.</li>
      <li><svg width="8" height="7" viewBox="0 0 8 7"><path d="M1 3.5l2 2L7 1" fill="none" stroke="var(--tick)" stroke-width="1.8"/></svg>Duis placerat eros ut metus suscipit non ultricies blandit.</li>
      <li><svg width="8" height="7" viewBox="0 0 8 7"><path d="M1 3.5l2 2L7 1" fill="none" stroke="var(--tick)" stroke-width="1.8"/></svg>Nunc elementum lacus in turpis accumsan ut feugiat.</li>
      <li><svg width="8" height="7" viewBox="0 0 8 7"><path d="M1 3.5l2 2L7 1" fill="none" stroke="var(--tick)" stroke-width="1.8"/></svg>Ut vitae velit id nisi dictum fermentum et nec arcu.</li>
    </ul>
  </section>
  <div class="abs ribbon">REGISTER YOUR DOMAIN HERE</div>
</main>

<div class="abs partners" aria-label="Technology partners">
  <div class="partner" style="width:46px;border-radius:50%"></div>
  <div class="partner" style="width:34px"></div>
  <div class="partner" style="width:58px"></div>
  <div class="partner" style="width:44px;height:32px"></div>
  <div class="partner" style="width:82px"></div>
  <div class="partner" style="width:50px"></div>
</div>

<footer class="abs site-footer">
  <div class="abs foot-col" style="left:13px">
    <h5>Web Hosting</h5>
    <ul><li>Fenestra or Penguix?</li><li>Penguix Hosting</li><li>Fenestra Hosting</li><li>SSL Certificates</li><li>Advanced WebMail</li><li>Active Spam Filtering</li><li>Hosting Control Panel</li><li>Application Vault</li></ul>
  </div>
  <div class="abs foot-col" style="left:104px">
    <h5>VPS Virtual Servers</h5>
    <ul><li>Penguix VPS</li><li>Fenestra VPS</li><li>Fenestra Plexo VPS</li><li>Penguix Plexo VPS</li><li>Plexo Hosting VPS</li><li>CtrlDesk Virtual Servers</li><li>Quickstart Add-on</li><li>CtrlDesk VPS</li><li>Zar VPS</li><li>HyperVista VPS</li></ul>
  </div>
  <div class="abs foot-col" style="left:198px">
    <h5>Dedicated Servers</h5>
    <ul><li>Special Offers</li><li>Same Day Dedicated</li><li>Small Business Servers</li><li>Medium Business Servers</li><li>Enterprise Servers</li><li>Fenestra Dedicated Servers</li><li>Backup and Recovery</li><li>Data Center</li><li>Remote Access / Reboot</li><li>Dedicated Server FAQ</li><li>Request a Quote</li></ul>
  </div>
  <div class="abs foot-col" style="left:308px">
    <h5>About Nimbo58</h5>
    <ul><li>About Nimbo58</li><li>Partners</li><li>Terms of Service</li><li>Service Level Agreement</li><li>Privacy Policy</li><li>Refund Policy</li><li>Jobs @ Nimbo58</li><li>Contact Us</li></ul>
  </div>
  <div class="abs foot-divider"></div>
  <div class="abs social">
    <h5>Let's Be Social!</h5>
    <div class="social-row"><span class="social-square" style="background:#5bb5e6"></span>Follow us on Chirpr</div>
    <div class="social-row"><span class="social-square" style="background:#3b5a98"></span>Become a fan on Facepage</div>
  </div>
  <p class="abs copyright">© 2012 Nimbo58. All rights reserved<br><a>Privacy</a> | <a>Sitemap</a></p>
</footer>

</body>
</html>
```